New Business Card (to reflect updated website content and graphics)

I changed some text and graphics on my website, so I need a new business card.

Target Market(s)

Mostly women, ages 30 - 60.

Industry/Entity Type

Life Coaching

Contact Information for Business Card

Included in attached Word document

Font styles to use
Sans Serif

Requirements
Must have
• I am not a creative person, so I will defer to designer. Take a look at my website, and you can get a feel for me, my style, and my target audience. Thank You!

My 3 branding colors are included in attached Word document.

```html
<!DOCTYPE html>
<html lang="en">
<head>
<meta charset="utf-8">
<title>Harbor Heart Coaching – Business Card</title>
<link href="https://fonts.googleapis.com/css2?family=Questrial&family=Lora:wght@400&family=Allura&display=swap" rel="stylesheet">
<style>
  :root {
    --bg: #5a5f6b;
    --teal: #2796b0;
    --white: #ffffff;
    --blush: #f6e3ec;
    --cream: #fbf8ea;
    --lavender: #e3e6f6;
    --peach: #f7e6e1;
    --coral: #e8776b;
  }
  * { box-sizing: border-box; margin: 0; padding: 0; }
  html, body { width: 1200px; height: 946px; overflow: hidden; }
  body { background: var(--bg); font-family: "Questrial", sans-serif; position: relative; }

  .card {
    position: absolute;
    width: 620px; height: 354px;
    border-radius: 28px;
    overflow: hidden;
    box-shadow: 0 14px 30px rgba(0,0,0,.35);
  }

  /* Front */
  .card--front {
    left: 70px; top: 90px;
    background: linear-gradient(115deg, var(--blush) 0%, var(--cream) 45%, var(--lavender) 75%, var(--peach) 100%);
  }
  .word-cloud-area {
    position: absolute;
    left: 220px; top: 44px;
    width: 180px; height: 150px;
    border-radius: 14px;
    background: linear-gradient(135deg, rgba(39,150,176,.30) 0%, rgba(232,119,107,.26) 50%, rgba(39,150,176,.30) 100%);
  }
  .tagline {
    position: absolute;
    left: 0; right: 0; top: 226px;
    text-align: center;
    font-family: "Allura", cursive;
    font-size: 46px;
    line-height: 1.2;
    color: var(--teal);
  }

  /* Back */
  .card--back {
    left: 510px; top: 500px;
    background: var(--white);
  }
  .card--back .band {
    position: absolute; inset: 0;
  }
  .brand {
    position: absolute;
    left: 0; right: 0; top: 70px;
    text-align: center;
    font-size: 30px;
    letter-spacing: 2px;
    color: var(--teal);
  }
  .holder-name {
    position: absolute;
    left: 96px; top: 204px;
    font-size: 28px;
    color: var(--white);
    letter-spacing: .5px;
  }
  .credentials {
    position: absolute;
    left: 350px; top: 196px;
    list-style: none;
    font-family: "Lora", serif;
    font-size: 13px;
    color: var(--white);
  }
  .credentials li, .contacts li {
    display: flex; align-items: center; gap: 9px;
    margin-bottom: 8px;
  }
  .contacts {
    position: absolute;
    left: 40px; top: 266px;
    list-style: none;
    font-family: "Lora", serif;
    font-size: 14px;
    color: var(--white);
  }
  .icon { width: 18px; height: 18px; flex: none; }
</style>
</head>
<body>

<section class="card card--front">
  <div class="word-cloud-area" role="img" aria-label="Heart-shaped word cloud of wellbeing words such as hope, joy, love, peace and clarity"></div>
  <p class="tagline">True Happiness Comes From Within</p>
</section>

<section class="card card--back">
  <svg class="band" viewBox="0 0 620 354" width="620" height="354" aria-hidden="true">
    <polygon points="0,180 620,160 620,354 0,354" fill="var(--teal)"/>
  </svg>

  <p class="brand">Harbor Heart Coaching</p>
  <p class="holder-name">Marla Vensen</p>

  <ul class="credentials">
    <li><svg class="icon" viewBox="0 0 18 18"><circle cx="9" cy="9" r="9" fill="#fff"/><path d="M5 9.2l2.6 2.6L13 6.5" stroke="var(--teal)" stroke-width="2" fill="none"/></svg>Certified Professional Life Coach</li>
    <li><svg class="icon" viewBox="0 0 18 18"><circle cx="9" cy="9" r="9" fill="#fff"/><path d="M5 9.2l2.6 2.6L13 6.5" stroke="var(--teal)" stroke-width="2" fill="none"/></svg>Health &amp; Wellness Coach</li>
    <li><svg class="icon" viewBox="0 0 18 18"><circle cx="9" cy="9" r="9" fill="#fff"/><path d="M5 9.2l2.6 2.6L13 6.5" stroke="var(--teal)" stroke-width="2" fill="none"/></svg>Advanced Grief Support Specialist</li>
  </ul>

  <ul class="contacts">
    <li><svg class="icon" viewBox="0 0 18 18"><circle cx="9" cy="9" r="9" fill="#fff"/><path d="M6 5c1 0 1.5 2 1 2.6-.4.4 1.4 2.6 2.4 2.8.6-.6 2.6 0 2.6 1 0 1-1.5 1.6-2.4 1.2C7.5 11.8 5.3 9.4 5 7.4 4.8 6 5.2 5 6 5z" fill="var(--teal)"/></svg>(555) 014-2273</li>
    <li><svg class="icon" viewBox="0 0 18 18"><circle cx="9" cy="9" r="9" fill="#fff"/><rect x="4.5" y="6" width="9" height="6.5" rx="1" fill="var(--teal)"/><path d="M4.8 6.4L9 9.6l4.2-3.2" stroke="#fff" stroke-width="1" fill="none"/></svg>marla@harborheartcoaching.com</li>
    <li><svg class="icon" viewBox="0 0 18 18"><circle cx="9" cy="9" r="9" fill="#fff"/><circle cx="9" cy="9" r="4.5" fill="none" stroke="var(--teal)" stroke-width="1.3"/><path d="M4.5 9h9M9 4.5c-2 2.6-2 6.4 0 9M9 4.5c2 2.6 2 6.4 0 9" stroke="var(--teal)" stroke-width="1" fill="none"/></svg>www.harborheartcoaching.com</li>
  </ul>
</section>

</body>
</html>
```